Business Consulting Business Card

professional business card with basic information (1) First and Last name (2) email address, (3) phone number, (4) website.

```html
<!DOCTYPE html>
<html lang="en">
<head>
<meta charset="utf-8">
<title>Tide Harbor — Business Card</title>
<link rel="stylesheet" href="https://fonts.googleapis.com/css2?family=Poppins:wght@400;500;700&display=swap">
<style>
  :root {
    --canvas: #d8d3cb;
    --card-light: #f2f2f2;
    --band-teal: #a3d5d3;
    --ink-navy: #0b2b40;
    --card-navy: #082a40;
    --mark-teal: #3fb3bf;
    --white: #ffffff;
  }
  * { margin: 0; padding: 0; box-sizing: border-box; }
  html, body {
    width: 900px; height: 1200px; overflow: hidden;
    background: var(--canvas);
    font-family: "Poppins", sans-serif;
  }
  .stage { position: relative; width: 900px; height: 1200px; }

  .card {
    position: absolute; left: 75px; width: 768px;
    border-radius: 18px; overflow: hidden;
  }
  .card--front { top: 133px; height: 438px; background: var(--card-light); }
  .card--back { top: 627px; height: 441px; background: var(--card-navy); }

  .brand { position: absolute; display: flex; align-items: center; }
  .brand__dot { border-radius: 50%; background: var(--mark-teal); flex: none; }
  .brand__name { font-weight: 400; letter-spacing: 0.16em; white-space: nowrap; }

  .card--front .brand { left: 175px; top: 72px; }
  .card--front .brand__dot { width: 72px; height: 72px; margin-right: 26px; }
  .card--front .brand__name { font-size: 39px; color: var(--ink-navy); }

  .card--back .brand { left: 147px; top: 168px; }
  .card--back .brand__dot { width: 84px; height: 84px; margin-right: 28px; }
  .card--back .brand__name { font-size: 44px; color: var(--white); }

  .contact-band {
    position: absolute; left: 0; top: 223px; width: 100%; height: 182px;
    background: var(--band-teal);
  }
  .holder-name {
    position: absolute; left: 63px; top: 66px;
    font-size: 25px; font-weight: 700; color: var(--ink-navy);
  }
  .contact-list { position: absolute; left: 406px; top: 32px; list-style: none; }
  .contact-list li {
    display: flex; align-items: flex-start;
    font-size: 21px; line-height: 27px; color: var(--ink-navy);
  }
  .contact-list li + li { margin-top: 0; }
  .contact-list li.address { margin-top: 10px; }
  .contact-list svg { width: 24px; height: 24px; margin: 1px 16px 0 0; fill: var(--ink-navy); flex: none; }

  .website {
    position: absolute; left: 0; width: 100%; top: 373px;
    text-align: center; font-size: 20px; letter-spacing: 0.16em;
    color: var(--white);
  }
</style>
</head>
<body>
<main class="stage">
  <section class="card card--front">
    <div class="brand">
      <span class="brand__dot"></span>
      <span class="brand__name">TIDE HARBOR</span>
    </div>
    <div class="contact-band">
      <h1 class="holder-name">MARCUS ELLERY</h1>
      <ul class="contact-list">
        <li>
          <svg viewBox="0 0 24 24" aria-hidden="true"><path d="M3 8c0-2 4-4 9-4s9 2 9 4v2h-5V8H8v2H3zM6 11h12l2 8H4z"/><circle cx="12" cy="15" r="2" fill="#a3d5d3"/></svg>
          01 98 76 5432
        </li>
        <li>
          <svg viewBox="0 0 24 24" aria-hidden="true"><path d="M3 6h18v12H3z"/><path d="M3 6l9 7 9-7" fill="none" stroke="#a3d5d3" stroke-width="1.6"/></svg>
          info@tideharbor.com
        </li>
        <li class="address">
          <svg viewBox="0 0 24 24" aria-hidden="true"><path d="M12 2a7 7 0 0 0-7 7c0 5 7 13 7 13s7-8 7-13a7 7 0 0 0-7-7zm0 9.5A2.5 2.5 0 1 1 12 6.5a2.5 2.5 0 0 1 0 5z"/></svg>
          <span>1475 bayview lane<br>tampa, FL 33602</span>
        </li>
      </ul>
    </div>
  </section>

  <section class="card card--back">
    <div class="brand">
      <span class="brand__dot"></span>
      <span class="brand__name">TIDE HARBOR</span>
    </div>
    <p class="website">WWW.TIDEHARBOR.COM</p>
  </section>
</main>
</body>
</html>
```